Design One Page Cheat Sheet

Require a design that will be used across a range of cheat sheets.
These cheat sheets are on 1 page, A4 size and provide tips for a young professionals career. Examples to design are attached.

Seeking a professional but creative, trendy look.

Our company is a site where young professionals go to access high quality career tools. The age of our customers range from 20-30 across a range of industries.

Files must be submitted in PDF and InDesign format.

Please use Bright Harbor logo. See two options attached.
Mandatory use of all 3 corporate colours is required.
R66 G73 B74 (Grey)
R242 G240 B230 (Off-white)
R38 G128 B138 (Teal)

Target Market(s)

20-30

Requirements
Must have
• Full Logo
• Mandatory use of all 3 corporate colours is required.
• R66 G73 B74 (Grey)
• R242 G240 B230 (Off-white)
• R38 G128 B138 (Teal)
• Bottom of cheat sheet must display Copyright Bright Harbor 2015
• Tweet us @BrightHarbor using #keenisgood and tell us what you think!

```html
<!DOCTYPE html>
<html lang="en">
<head>
<meta charset="utf-8">
<title>9 Words to use with your Bank – Cheat Sheet</title>
<link href="https://fonts.googleapis.com/css2?family=Montserrat:wght@400;600;700&family=Open+Sans:wght@400;600;700&display=swap" rel="stylesheet">
<style>
  :root {
    --grey: #42494a;
    --offwhite: #f2f0e6;
    --teal: #26808a;
    --backdrop: #dedee2;
    --white: #ffffff;
    --body-text: #3d4445;
  }
  * { box-sizing: border-box; margin: 0; padding: 0; }
  html, body { width: 1200px; height: 1000px; overflow: hidden; }
  body {
    background: var(--backdrop);
    font-family: "Open Sans", Arial, sans-serif;
    color: var(--body-text);
  }
  .sheet {
    position: absolute;
    left: 268px; top: 30px;
    width: 664px; height: 940px;
    background: var(--white);
    box-shadow: 0 6px 24px rgba(0,0,0,.18);
    display: flex; flex-direction: column;
  }
  .sheet__topband { height: 14px; background: var(--teal); }
  .sheet__header { padding: 20px 36px 12px; }
  .title {
    display: flex; align-items: center; gap: 12px;
    font-family: "Montserrat", Arial, sans-serif;
    font-weight: 700; font-size: 30px; color: var(--teal);
  }
  .title__number {
    width: 42px; height: 42px;
    background: var(--grey); color: var(--white);
    display: flex; align-items: center; justify-content: center;
    font-size: 30px; border: 3px solid var(--teal);
  }
  .intro {
    margin-top: 12px;
    font-weight: 700; font-size: 11px; line-height: 15px; color: var(--grey);
  }
  .tips { padding: 0 36px; display: flex; flex-direction: column; gap: 6px; }
  .tip { background: var(--offwhite); }
  .tip__label {
    background: var(--grey); color: var(--white);
    font-weight: 700; font-size: 9px; letter-spacing: .3px;
    padding: 2px 10px; height: 15px; line-height: 11px;
    border-top: 3px solid #5a6163;
  }
  .tip__text { font-size: 8.2px; line-height: 11px; padding: 5px 10px 6px; }
  .brand {
    display: flex; justify-content: flex-end; align-items: center; gap: 8px;
    padding: 12px 36px 0;
  }
  .brand__mark { width: 26px; height: 26px; border-radius: 50%; border: 2px solid var(--teal); }
  .brand__name {
    font-family: "Montserrat", Arial, sans-serif; font-weight: 700;
    font-size: 20px; color: var(--teal); letter-spacing: 1px; text-transform: uppercase;
  }
  .copyright { text-align: right; font-size: 8px; padding: 4px 36px 0; color: var(--grey); }
  .footer { margin-top: auto; }
  .footer__band-teal { height: 14px; background: var(--teal); }
  .footer__band-grey { height: 8px; background: var(--grey); margin-top: 4px; }
  .social { padding: 14px 36px 18px; display: flex; flex-direction: column; gap: 6px; }
  .social__line {
    display: flex; align-items: center; gap: 10px;
    font-weight: 700; font-size: 14px; color: var(--grey);
  }
  .social__square { width: 14px; height: 14px; background: var(--teal); }
  .social__square--alt { background: #c0392b; }
</style>
</head>
<body>
<main class="sheet">
  <div class="sheet__topband"></div>
  <header class="sheet__header">
    <h1 class="title"><span class="title__number">9</span>Words to use with your Bank...</h1>
    <p class="intro">Keen to access a better interest rate, gain more flexibility and extra benefits? Get financially savvy and use these words to negotiate a superior deal.</p>
  </header>

  <section class="tips">
    <article class="tip"><h2 class="tip__label">Loyalty</h2><p class="tip__text">Longstanding customers are an investment to a bank's balance sheet. You might just think you're one person but there's a million more just like you. Collectively your balances draw growth to their bottom line. Customers who show loyalty are rewarded. Remind your banker the tenure of your relationship. If they don't notice it then make them aware.</p></article>
    <article class="tip"><h2 class="tip__label">Income</h2><p class="tip__text">The more you earn the more value you create to a bank. Young adults earning good money are in the wealth accumulation stage of their financial lifecycle. Which means as your career and income stream prosper so too does the bank collecting the salary credit.</p></article>
    <article class="tip"><h2 class="tip__label">Collateral</h2><p class="tip__text">In banking-lingo this is more likely referred to as 'gift banking' but as a consumer view your other business held elsewhere as collateral. When in negotiations psychology tells us people need to feel like they're winning to give something away. Collateral such as a personal loan, credit card, salary account, home loan, insurance or savings is more business to the bank. Offer it up on the basis you get something in return.</p></article>
    <article class="tip"><h2 class="tip__label">Insurance</h2><p class="tip__text">Consumers or business owners need to understand that for banks, insurance is both a risk mitigation strategy and a strong income stream. In most cases insurance reduces your risk profile resulting in a better interest rate. For you as the customer it offers peace of mind and protects your cash flow in times of need. Worth considering: income protection insurance or business insurance.</p></article>
    <article class="tip"><h2 class="tip__label">Mortgage</h2><p class="tip__text">Buying your own home is a goal for most people. Whether you're at first stage or saving to get there tell your bank. They're always looking to grow their lending book and will often have special offers going that you might be able to benefit from. If they don't know you're in the market then you may miss out.</p></article>
    <article class="tip"><h2 class="tip__label">Competitor</h2><p class="tip__text">Find yourself not getting anywhere with your bank? Advise them you're considering a competitor. Do your research prior and find at least 2 better offers in the marketplace. Provide your evidence. Be prepared though – you might get a better deal or they might let you go.</p></article>
    <article class="tip"><h2 class="tip__label">Friends</h2><p class="tip__text">Customers should never be viewed as a singular transaction. Everyone has friends, colleagues and family that they will share their banking experience with. Whether things are going in your favor or not slip into the conversation that you have a friend who would be thrilled to receive this or shocked about your experience. Leverage. If it's a good banker they will want a referral to the friend.</p></article>
    <article class="tip"><h2 class="tip__label">Online</h2><p class="tip__text">The world is changing and everyone is online. Banking customers who transact online are cost effective and low on demand. Make sure you're online. Customers that don't ask for much have a good track record of getting something when they finally do.</p></article>
    <article class="tip"><h2 class="tip__label">Future</h2><p class="tip__text">Share your future financial goals with your bank. It's likely to be stored in a CRM system somewhere and it might assist with you getting better service. If they believe they can obtain greater value out of you then your relationship will be catered to.</p></article>
  </section>

  <div class="brand"><span class="brand__mark"></span><span class="brand__name">Bright Harbor</span></div>
  <p class="copyright">© Copyright Bright Harbor 2015</p>

  <footer class="footer">
    <div class="footer__band-teal"></div>
    <div class="footer__band-grey"></div>
    <div class="social">
      <p class="social__line"><span class="social__square"></span>Tweet us @BrightHarbor</p>
      <p class="social__line"><span class="social__square social__square--alt"></span>#keenisgood and tell us what you think!</p>
    </div>
    <div class="footer__band-teal"></div>
  </footer>
</main>
</body>
</html>
```